Brantley Advisory Group provides support for renewable energy projects to utilities and suppliers

I need a professional looking business card that is both simple and elegant and unique. My clients are mostly large organizations not individuals. I am a consultant with my own company that is small but would like to give clients the impression I am larger. Smart grid, fiber optics, software, field hardware, distribution automation, substation automation, operations, energy storage/batteries, microgrids, customer service, strategy/roadmaps, conservation, Automated Metering Infrastruture (AMI or smart meters) are all areas of focus.

Target Market(s)

Utilities, suppliers, governmental agencies involved in energy. All types of energy especially natural gas and electrical. Especially renewable energy or green projects.

Contact Information for Business Card

Name - Ross Brantley Cell Phone - 425.318.4762 Email - rbrantley@brantleyag-example.com
Company - Brantley Advisory Group (logo) Title - Principal

Font styles to use
Serif
Sans Serif

Colors

Designer to choose colors to be used in the design.

Requirements
Must have
• Simple and professional and powerful.
• Unique/creative design.
Nice to have
• Utilize color scheme to accent logo colors. Maybe some geometric pattern on edge of card with color.
Should not have
• Busy, complicated, traditional

```html
<!DOCTYPE html>
<html lang="en">
<head>
<meta charset="utf-8">
<title>Brantley Advisory Group – Business Card</title>
<link rel="stylesheet" href="https://fonts.googleapis.com/css2?family=Montserrat:wght@600;700&family=Open+Sans:wght@400;600&display=swap">
<style>
  :root {
    --royal-blue: #1f3f9c;
    --pattern-blue: #2a4cab;
    --leaf-green: #6a9a3a;
    --ink-grey: #6b6e73;
    --rule-grey: #d9dadc;
    --paper: #ffffff;
    --backdrop: #ececec;
  }
  * { box-sizing: border-box; margin: 0; padding: 0; }
  html, body {
    width: 1200px;
    height: 1015px;
    overflow: hidden;
    background: var(--backdrop);
  }
  .stage {
    width: 1200px;
    height: 1015px;
    display: flex;
    flex-direction: column;
    align-items: center;
    justify-content: center;
    gap: 60px;
  }
  .card {
    width: 560px;
    height: 320px;
    position: relative;
    overflow: hidden;
    box-shadow: 0 10px 24px rgba(0,0,0,0.18);
  }

  /* Back side */
  .card-back {
    background: var(--royal-blue);
  }
  .card-back .pattern-field {
    position: absolute;
    inset: 0;
    background: linear-gradient(135deg, var(--royal-blue), var(--pattern-blue) 50%, var(--royal-blue));
  }
  .card-back .back-name {
    position: absolute;
    inset: 0;
    display: flex;
    align-items: center;
    justify-content: center;
    font-family: "Montserrat", sans-serif;
    font-weight: 600;
    font-size: 18px;
    letter-spacing: 0.04em;
    color: var(--paper);
  }

  /* Front side */
  .card-front {
    background: var(--paper);
    border-bottom: 9px solid var(--royal-blue);
    display: flex;
  }
  .brand-block {
    width: 300px;
    display: flex;
    align-items: center;
    justify-content: center;
    gap: 12px;
    padding-left: 20px;
  }
  .brand-square {
    width: 30px;
    height: 30px;
    background: var(--leaf-green);
    flex: none;
  }
  .brand-name {
    font-family: "Montserrat", sans-serif;
    font-weight: 700;
    font-size: 19px;
    line-height: 1.15;
    color: var(--royal-blue);
  }
  .divider {
    width: 1px;
    align-self: stretch;
    margin: 46px 0 60px;
    background: var(--rule-grey);
  }
  .contact-block {
    flex: 1;
    padding: 58px 0 0 20px;
  }
  .person-name {
    font-family: "Montserrat", sans-serif;
    font-weight: 700;
    font-size: 17px;
    letter-spacing: 0.02em;
    text-transform: uppercase;
    color: var(--royal-blue);
  }
  .person-title {
    font-family: "Open Sans", sans-serif;
    font-size: 13px;
    color: var(--ink-grey);
    margin-top: 1px;
  }
  .contact-list {
    list-style: none;
    margin-top: 18px;
    font-family: "Open Sans", sans-serif;
    font-size: 11.5px;
    color: var(--ink-grey);
  }
  .contact-list li {
    display: flex;
    align-items: center;
    gap: 7px;
    line-height: 19px;
  }
  .contact-list svg { width: 11px; height: 11px; flex: none; }
</style>
</head>
<body>
<main class="stage">
  <section class="card card-back" aria-label="Card back">
    <div class="pattern-field" role="img" aria-label="Repeating pattern of overlapping outlined squares in lighter blue"></div>
    <p class="back-name">Brantley Advisory Group</p>
  </section>

  <section class="card card-front" aria-label="Card front">
    <div class="brand-block">
      <span class="brand-square" aria-hidden="true"></span>
      <p class="brand-name">Brantley<br>Advisory Group</p>
    </div>
    <div class="divider" aria-hidden="true"></div>
    <div class="contact-block">
      <h1 class="person-name">Ross Brantley</h1>
      <p class="person-title">Principal</p>
      <ul class="contact-list">
        <li>
          <svg viewBox="0 0 12 12" aria-hidden="true"><path fill="#1f3f9c" d="M1 4c0-2 2-3 5-3s5 1 5 3l-2 1-1-1.5H4L3 5 1 4zm2 2h6l1 5H2l1-5zm3 1a1.3 1.3 0 100 2.6A1.3 1.3 0 006 7z"/></svg>
          425.318.4762
        </li>
        <li>
          <svg viewBox="0 0 12 12" aria-hidden="true"><rect x="1" y="2.5" width="10" height="7" fill="#9a9da2"/><path d="M1 2.5l5 4 5-4" fill="none" stroke="#fff" stroke-width="1"/></svg>
          rbrantley@brantleyag-example.com
        </li>
        <li>
          <svg viewBox="0 0 12 12" aria-hidden="true"><circle cx="6" cy="6" r="5.5" fill="#6a9a3a"/><path d="M3 4c1 0 2 1 2 2s1 2 0 3M7 2.5c1 1 2 1.5 1.5 3" fill="none" stroke="#fff" stroke-width="1"/></svg>
          www.brantleyag-example.com
        </li>
      </ul>
    </div>
  </section>
</main>
</body>
</html>
```